Road Construction Company needs business cards

We would like a new business card designed for our business.

We're a road construction company based in Qld, Australia.

Can the business card please have the following information on it.

Name: Brent Halloway
Position: General Manager
Phone: 0491 257 314
Email: Brent.halloway@drovik.com.au
Address: 87 Margrove Ave, Tindale, QLD, 4016
Website: www.drovik.com.au

Visually we'd like the card to be professional and simple.

Attached is our logo.

Our website is www.drovik.com.au

Target Market(s)

Men aged 25-60

Contact Information for Business Card

As listed in project description

Font styles to use
Serif

Requirements
Must have
• Large logo on back of card

```html
<!DOCTYPE html>
<html lang="en">
<head>
<meta charset="utf-8">
<title>Drovik Business Card</title>
<link rel="stylesheet" href="https://fonts.googleapis.com/css2?family=Exo+2:wght@400;800&display=swap">
<style>
  :root {
    --stage: #2a2a2a;
    --card-dark: #1a1a1a;
    --card-light: #ffffff;
    --brand-blue: #0b4fa3;
    --accent-blue: #2a8fd6;
    --ink: #111111;
    --rule: #9a9a9a;
    --dark-mark: #4a4a4a;
  }
  html, body {
    margin: 0;
    width: 1200px;
    height: 1040px;
    overflow: hidden;
    background: var(--stage);
    font-family: "Exo 2", sans-serif;
  }
  .stage {
    position: relative;
    width: 1200px;
    height: 1040px;
  }
  .card {
    position: absolute;
    left: 270px;
    width: 660px;
    height: 390px;
    border-radius: 0 80px 0 80px;
    box-shadow: 0 14px 30px rgba(0,0,0,0.55);
  }
  .card--back {
    top: 70px;
    background: var(--card-dark);
    display: flex;
    align-items: center;
    justify-content: center;
  }
  .card--front {
    top: 560px;
    background: var(--card-light);
  }
  .brand-name {
    font-family: "Exo 2", sans-serif;
    font-weight: 800;
    letter-spacing: 4px;
    line-height: 1;
  }
  .card--back .brand-name {
    font-size: 68px;
    color: var(--dark-mark);
  }
  .card--front .brand-name {
    position: absolute;
    left: 70px;
    top: 150px;
    font-size: 58px;
    color: var(--brand-blue);
  }
  .divider {
    position: absolute;
    left: 345px;
    top: 110px;
    width: 1px;
    height: 170px;
    background: var(--rule);
  }
  .details {
    position: absolute;
    left: 370px;
    top: 108px;
    color: var(--ink);
  }
  .person-name {
    margin: 0;
    font-weight: 800;
    font-size: 25px;
    letter-spacing: 2px;
    text-transform: uppercase;
    color: var(--brand-blue);
  }
  .person-role {
    margin: 0 0 14px;
    font-size: 19px;
    color: var(--accent-blue);
  }
  .contact-list {
    list-style: none;
    margin: 0 0 12px;
    padding: 0;
    font-size: 18px;
  }
  .contact-list li {
    display: flex;
    align-items: center;
    gap: 10px;
    height: 26px;
  }
  .contact-list svg {
    width: 16px;
    height: 16px;
    fill: var(--brand-blue);
    flex: none;
  }
  .web-domain { color: var(--brand-blue); }
  .address {
    margin: 0;
    font-style: normal;
    font-size: 18px;
    line-height: 1.35;
  }
</style>
</head>
<body>
<main class="stage">
  <section class="card card--back">
    <span class="brand-name">DROVIK</span>
  </section>

  <section class="card card--front">
    <span class="brand-name">DROVIK</span>
    <div class="divider"></div>
    <div class="details">
      <h1 class="person-name">Brent Halloway</h1>
      <p class="person-role">General Manager</p>
      <ul class="contact-list">
        <li>
          <svg viewBox="0 0 24 24" aria-hidden="true"><path d="M6.6 10.8a15.1 15.1 0 0 0 6.6 6.6l2.2-2.2a1 1 0 0 1 1-.25 11.4 11.4 0 0 0 3.6.57 1 1 0 0 1 1 1V20a1 1 0 0 1-1 1A17 17 0 0 1 3 4a1 1 0 0 1 1-1h3.5a1 1 0 0 1 1 1c0 1.25.2 2.45.57 3.57a1 1 0 0 1-.25 1z"/></svg>
          0491 257 314
        </li>
        <li>
          <svg viewBox="0 0 24 24" aria-hidden="true"><path d="M2 5h20v14H2z M2 5l10 8 10-8" fill="var(--brand-blue)" stroke="#fff" stroke-width="1.5"/></svg>
          Brent.halloway@drovik.com.au
        </li>
        <li>
          <svg viewBox="0 0 24 24" aria-hidden="true"><circle cx="12" cy="12" r="9" fill="none" stroke="var(--brand-blue)" stroke-width="2"/><path d="M3 12h18M12 3c3 3 3 15 0 18M12 3c-3 3-3 15 0 18" fill="none" stroke="var(--brand-blue)" stroke-width="1.6"/></svg>
          <span>www.<span class="web-domain">drovik</span>.com.au</span>
        </li>
      </ul>
      <address class="address">87 Margrove Ave<br>Tindale, QLD, 4016</address>
    </div>
  </section>
</main>
</body>
</html>
```